Postcard Design

I am an attorney in Pittsburgh. Here and across country, companies are sending data with names, address and new criminal charges for people. This has resulted in some people getting 12 or more of these letters. I want to do a postcard because one does not need to open a postcard. I also want to be delicate since there is no sealed envelope. I want to throw in other matters other than criminal so it does not look like the person is necessarily charged with a crime.
At top would be "Law Office of Dennis K. Varholtz"
Then:
Need an Attorney?
Attorney Dennis K. Varholtz has 25 Years of Experience
Free Consultation - Affordable Fees - Credit Cards Accepted
-All Criminal Matters
-Most Civil Matters
-DUI / Traffic Citations / License Restoration
412-555-0187
www.harbordefensecounsel.example
www.dkvcounsel.example

My CTQ ranking is A+ but I am not sure they give a logo with the rating. I have all my logos at www.harbordefensecounsel.example The purpose of the two websites is these are postcards. I want no one to think oh this person is charged with a crime.

```html
<!DOCTYPE html>
<html lang="en">
<head>
<meta charset="utf-8">
<title>Law Office of Dennis K. Varholtz – Postcard</title>
<link rel="stylesheet" href="https://fonts.googleapis.com/css2?family=Crimson+Pro:wght@400;600;700&family=Source+Sans+3:wght@400;600&display=swap">
<style>
  :root {
    --maroon: #5a1014;
    --maroon-dark: #3f0a0d;
    --gold: #a9842f;
    --gold-light: #e6cf8a;
    --gold-pale: #f3ead0;
    --cream: #fbf8f1;
    --ink: #151515;
    --white: #ffffff;
    --seal-navy: #1e2f63;
    --badge-blue: #2a59a8;
  }
  * { margin: 0; padding: 0; box-sizing: border-box; }
  html, body { width: 1200px; height: 800px; overflow: hidden; }
  body { background: #e9e9e9; }

  .postcard {
    position: relative;
    width: 1200px;
    height: 800px;
    overflow: hidden;
    background: var(--cream);
    font-family: "Source Sans 3", Arial, sans-serif;
  }
  .postcard__shapes { position: absolute; inset: 0; }

  .portrait {
    position: absolute; left: 22px; top: 20px; width: 290px; height: 142px;
    background: linear-gradient(135deg, #9fb2c9 0%, #d8dde4 55%, #8a98a8 100%);
    border: 3px solid var(--gold-light);
  }
  .gavel {
    position: absolute; left: 880px; top: 560px; width: 280px; height: 210px;
    background: radial-gradient(ellipse at 45% 55%, #9a5a2e 0%, #c9a978 60%, rgba(255,255,255,0) 75%);
  }

  .header__kicker {
    position: absolute; left: 482px; top: 46px;
    font-family: "Source Sans 3", Arial, sans-serif;
    font-size: 28px; letter-spacing: 1px; color: var(--white);
    white-space: nowrap;
  }
  .header__title {
    position: absolute; left: 480px; top: 88px; width: 700px;
    font-family: "Crimson Pro", Georgia, serif; font-weight: 700;
    font-size: 47px; line-height: 1.1; color: var(--white); white-space: nowrap;
  }

  .headline {
    position: absolute; left: 355px; top: 222px;
    font-family: "Crimson Pro", Georgia, serif; font-weight: 700;
    font-size: 106px; line-height: 1; color: var(--gold);
    white-space: nowrap;
  }
  .experience {
    position: absolute; left: 360px; top: 336px;
    font-family: "Crimson Pro", Georgia, serif; font-weight: 600;
    font-size: 32px; color: var(--gold); white-space: nowrap;
  }
  .services {
    position: absolute; left: 360px; top: 388px; list-style: none;
    font-family: "Source Sans 3", Arial, sans-serif; font-weight: 600;
    font-size: 32px; line-height: 48px; color: var(--ink); white-space: nowrap;
  }
  .services .star { color: var(--maroon); font-size: 24px; margin: 0 8px; }
  .site-main {
    position: absolute; left: 360px; top: 494px;
    font-family: "Crimson Pro", Georgia, serif; font-weight: 700;
    font-size: 32px; color: var(--ink); white-space: nowrap;
  }

  .contact {
    position: absolute; left: 40px; top: 585px; list-style: none;
    font-size: 24px; line-height: 36px; color: var(--white); white-space: nowrap;
  }
  .contact__label { color: var(--gold-pale); }
  .benefits {
    position: absolute; left: 40px; top: 728px;
    font-size: 28px; color: var(--white); white-space: nowrap;
  }
  .benefits .star { font-size: 20px; margin: 0 10px; color: var(--gold-light); }
</style>
</head>
<body>
<main class="postcard">
  <svg class="postcard__shapes" width="1200" height="800" viewBox="0 0 1200 800" aria-hidden="true">
    <defs>
      <linearGradient id="header-fill" x1="0" y1="0" x2="1" y2="0">
        <stop offset="0" stop-color="var(--maroon-dark)"/>
        <stop offset="0.6" stop-color="var(--maroon)"/>
        <stop offset="1" stop-color="#a88a84"/>
      </linearGradient>
      <linearGradient id="gold-fill" x1="0" y1="0" x2="1" y2="1">
        <stop offset="0" stop-color="#b8933c"/>
        <stop offset="0.5" stop-color="var(--gold-light)"/>
        <stop offset="1" stop-color="#a47d2c"/>
      </linearGradient>
      <linearGradient id="body-fill" x1="0" y1="0" x2="1" y2="0">
        <stop offset="0" stop-color="var(--white)"/>
        <stop offset="1" stop-color="#ece8e2"/>
      </linearGradient>
      <linearGradient id="band-fill" x1="0" y1="0" x2="0" y2="1">
        <stop offset="0" stop-color="var(--maroon)"/>
        <stop offset="1" stop-color="var(--maroon-dark)"/>
      </linearGradient>
    </defs>
    <rect x="330" y="200" width="870" height="600" fill="url(#body-fill)"/>
    <rect x="0" y="0" width="330" height="560" fill="url(#gold-fill)"/>
    <rect x="330" y="0" width="870" height="192" fill="url(#header-fill)"/>
    <rect x="330" y="192" width="870" height="5" fill="var(--gold)"/>
    <circle cx="400" cy="88" r="66" fill="var(--seal-navy)" stroke="var(--gold-light)" stroke-width="6"/>
    <circle cx="400" cy="88" r="44" fill="none" stroke="var(--gold-light)" stroke-width="2"/>
    <circle cx="90" cy="250" r="56" fill="var(--badge-blue)" stroke="var(--gold-light)" stroke-width="4"/>
    <polygon points="0,560 760,560 880,800 0,800" fill="url(#band-fill)"/>
    <line x1="40" y1="710" x2="800" y2="710" stroke="var(--gold)" stroke-width="2"/>
  </svg>

  <div class="portrait" role="img" aria-label="Portrait photograph of the attorney"></div>

  <header>
    <p class="header__kicker">PITTSBURGH CRIMINAL DEFENSE ATTORNEY</p>
    <h1 class="header__title">Law Office of Dennis K. Varholtz</h1>
  </header>

  <h2 class="headline">Need an Attorney?</h2>
  <p class="experience">Attorney Dennis K. Varholtz has 25 Years of Experience</p>
  <ul class="services">
    <li>All Criminal Matters<span class="star">★</span>Most Civil Matters</li>
    <li>DUI / Traffic Citations / License Restoration</li>
  </ul>
  <p class="site-main">www.harbordefensecounsel.example</p>

  <div class="gavel" role="img" aria-label="Illustration of a wooden gavel on a sound block"></div>

  <ul class="contact">
    <li><span class="contact__label">Office number:</span> 412-555-0187</li>
    <li><span class="contact__label">Email:</span> office@dkvcounsel.example</li>
    <li><span class="contact__label">Website:</span> www.dkvcounsel.example</li>
  </ul>
  <p class="benefits">Free Consultation<span class="star">★</span>Affordable Fees<span class="star">★</span>Credit Cards Accepted</p>
</main>
</body>
</html>
```